Tern Netlink Website

We're looking for a basic website and order form for our stripped down ISP, Tern Netlink.

The front page should be basic with our two plan options - we're open to pretty much any design, but one possibility is an image of New Zealand with two clouds above it (similar to the quick mockup attached).

Clicking on one of the plans will then take the user to a basic order form.

We will also need a contact, about, and support page.

Industry/Entity Type

Isp

```html
<!DOCTYPE html>
<html lang="en">
<head>
<meta charset="utf-8">
<title>Tern Netlink — Pure Broadband</title>
<link rel="stylesheet" href="https://fonts.googleapis.com/css2?family=Questrial&family=Arimo:wght@400;700&display=swap">
<style>
  :root {
    --green-deep: #2f9a1c;
    --green-mid: #1f9e4c;
    --teal: #0c9f7c;
    --teal-light: #5bb9a0;
    --price-green: #3a9a17;
    --button-green: #37a01a;
    --panel: rgba(10, 90, 60, 0.45);
    --white: #ffffff;
    --text-soft: #eaf6ee;
  }
  * { box-sizing: border-box; margin: 0; padding: 0; }
  html, body { width: 1200px; height: 889px; overflow: hidden; }
  body {
    position: relative;
    font-family: "Arimo", Arial, sans-serif;
    color: var(--white);
    background: linear-gradient(60deg, var(--green-deep) 0%, var(--green-mid) 45%, var(--teal) 100%);
  }
  .sky-sweep {
    position: absolute; inset: 0;
    background: linear-gradient(118deg, transparent 0 58%, rgba(255,255,255,0.08) 58% 64%, rgba(255,255,255,0.2) 100%);
    clip-path: polygon(600px 0, 1200px 0, 1200px 889px, 1000px 889px);
    pointer-events: none;
  }
  a { color: inherit; text-decoration: none; }

  .account-bar {
    position: absolute; left: 809px; top: 40px; width: 266px; height: 34px;
    background: var(--button-green); border-radius: 4px;
    display: flex; align-items: center; font-size: 14px;
  }
  .account-bar a { flex: 1; text-align: center; }
  .account-bar .divider { width: 1px; height: 18px; background: rgba(255,255,255,0.8); }

  .brand { position: absolute; left: 145px; top: 82px; }
  .brand-name { font-family: "Questrial", sans-serif; font-size: 34px; line-height: 40px; letter-spacing: 0.5px; }
  .brand-tagline { font-family: "Questrial", sans-serif; font-size: 12.5px; letter-spacing: 1.6px; margin-top: 5px; }

  .main-nav {
    position: absolute; right: 121px; top: 125px;
    display: flex; gap: 21px;
    font-family: "Questrial", sans-serif; font-size: 14px; letter-spacing: 0.4px;
  }

  .map-area {
    position: absolute; left: 800px; top: 178px; width: 220px; height: 520px;
    border-radius: 40px;
    background: linear-gradient(160deg, rgba(255,255,255,0.95), rgba(255,255,255,0.55));
  }

  .plan { position: absolute; text-align: center; }
  .plan-cloud { position: relative; width: 280px; height: 158px; }
  .plan-cloud svg { position: absolute; inset: 0; }
  .plan-price {
    position: absolute; left: 0; right: 0; top: 40px;
    color: var(--price-green); font-family: "Questrial", sans-serif;
  }
  .plan-price .amount { font-size: 60px; letter-spacing: -2px; }
  .plan-price .period { font-size: 23px; margin-left: 4px; }
  .plan-order {
    position: absolute; left: 0; right: 0; top: 108px;
    color: var(--price-green); font-weight: 700; font-size: 14px; letter-spacing: 0.3px;
  }
  .plan-speed { font-size: 22px; margin-top: 10px; }
  .plan-speed strong { font-size: 26px; }
  .plan--standard { left: 152px; top: 214px; }
  .plan--fast { left: 497px; top: 213px; }
  .plan--fast .plan-speed { margin-top: 11px; }
  .plan--fast .plan-speed strong { font-size: 29px; }

  .features {
    position: absolute; left: 125px; top: 498px; width: 960px; height: 312px;
    background: var(--panel); border-radius: 3px;
  }
  .feature { position: absolute; top: 44px; width: 250px; }
  .feature-icon { display: block; margin: 0 auto; height: 80px; }
  .feature-title { text-align: center; font-size: 17px; font-weight: 700; line-height: 22px; margin-top: 10px; }
  .feature-text { font-size: 13.5px; line-height: 16.5px; color: var(--text-soft); margin-top: 25px; padding-left: 20px; width: 235px; }
  .feature--video { left: 25px; }
  .feature--speed { left: 334px; }
  .feature--peak { left: 651px; }

  .footer-nav {
    position: absolute; left: 131px; top: 841px;
    display: flex; gap: 10px; font-size: 12px;
  }
  .footer-contact { position: absolute; right: 122px; top: 842px; font-size: 12px; }
</style>
</head>
<body>
  <div class="sky-sweep"></div>

  <div class="account-bar">
    <a href="#">My Account</a><span class="divider"></span><a href="#">Order Now</a>
  </div>

  <header class="brand">
    <div class="brand-name">Tern Netlink</div>
    <div class="brand-tagline">PURE BROADBAND. PURE SPEED. NO LIMITS</div>
  </header>

  <nav class="main-nav">
    <a href="#">HOME</a><a href="#">PRODUCTS</a><a href="#">PROMOS</a>
    <a href="#">PRICING</a><a href="#">SUPPORT</a><a href="#">CONTACT</a>
  </nav>

  <div class="map-area" role="img" aria-label="Map of New Zealand in white"></div>

  <a class="plan plan--standard" href="#">
    <div class="plan-cloud">
      <svg viewBox="0 0 280 158" width="280" height="158" aria-hidden="true">
        <g fill="#fff">
          <circle cx="50" cy="95" r="50"/><circle cx="95" cy="50" r="44"/>
          <circle cx="160" cy="45" r="45"/><circle cx="220" cy="70" r="50"/>
          <circle cx="235" cy="105" r="44"/><rect x="40" y="60" width="200" height="95" rx="40"/>
        </g>
      </svg>
      <div class="plan-price"><span class="amount">$95</span><span class="period">/month</span></div>
      <div class="plan-order">CLICK HERE TO ORDER</div>
    </div>
    <div class="plan-speed">up to <strong>30mbps</strong> down</div>
  </a>

  <a class="plan plan--fast" href="#">
    <div class="plan-cloud">
      <svg viewBox="0 0 280 158" width="280" height="150" aria-hidden="true">
        <g fill="#fff">
          <circle cx="50" cy="95" r="50"/><circle cx="95" cy="50" r="44"/>
          <circle cx="160" cy="45" r="45"/><circle cx="220" cy="70" r="50"/>
          <circle cx="235" cy="105" r="44"/><rect x="40" y="60" width="200" height="95" rx="40"/>
        </g>
      </svg>
      <div class="plan-price"><span class="amount">$99</span><span class="period">/month</span></div>
      <div class="plan-order">CLICK HERE TO ORDER</div>
    </div>
    <div class="plan-speed">up to <strong>100mbps</strong> down</div>
  </a>

  <section class="features">
    <article class="feature feature--video">
      <svg class="feature-icon" viewBox="0 0 104 78" width="104" aria-hidden="true">
        <rect x="0" y="0" width="104" height="78" rx="5" fill="#fff"/>
        <g fill="#1a7a4a">
          <rect x="10" y="4" width="9" height="7"/><rect x="28" y="4" width="9" height="7"/><rect x="46" y="4" width="9" height="7"/><rect x="64" y="4" width="9" height="7"/><rect x="82" y="4" width="9" height="7"/>
          <rect x="10" y="67" width="9" height="7"/><rect x="28" y="67" width="9" height="7"/><rect x="46" y="67" width="9" height="7"/><rect x="64" y="67" width="9" height="7"/><rect x="82" y="67" width="9" height="7"/>
          <rect x="8" y="15" width="88" height="48"/>
        </g>
        <circle cx="52" cy="39" r="15" fill="none" stroke="#fff" stroke-width="4"/>
        <path d="M47 31 L60 39 L47 47 Z" fill="#fff"/>
      </svg>
      <h2 class="feature-title">Crystal Clear High<br>Definition Video</h2>
      <p class="feature-text">With a network especially engineered for smooth streaming performance, enjoy HD videos as they load and play amazingly fast.</p>
    </article>

    <article class="feature feature--speed">
      <svg class="feature-icon" viewBox="0 0 106 80" width="106" aria-hidden="true">
        <rect x="9" y="0" width="88" height="64" rx="6" fill="#fff"/>
        <rect x="17" y="8" width="72" height="48" fill="#1a7a4a"/>
        <path d="M0 68 H106 V74 Q106 80 100 80 H6 Q0 80 0 74 Z" fill="#fff"/>
        <path d="M44 18 L44 42 L50 36 L55 46 L59 44 L54 34 L62 34 Z" fill="#fff"/>
      </svg>
      <h2 class="feature-title">Ultra-Fast Speeds<br>Across Multiple Devices</h2>
      <p class="feature-text">100mbps enables a whole family on tablets, laptops, desktops and smart TVs to watch online videos, game, surf and download at ultra-fast speeds.</p>
    </article>

    <article class="feature feature--peak">
      <svg class="feature-icon" viewBox="0 0 80 80" width="80" aria-hidden="true">
        <circle cx="40" cy="40" r="40" fill="#fff"/>
        <circle cx="40" cy="40" r="32" fill="#1a7a4a"/>
        <circle cx="40" cy="40" r="28" fill="none" stroke="#fff" stroke-width="2" stroke-dasharray="2 5.3"/>
        <path d="M40 16 V40 H27" fill="none" stroke="#fff" stroke-width="4" stroke-linecap="round"/>
        <circle cx="40" cy="40" r="4" fill="#fff"/>
      </svg>
      <h2 class="feature-title">Superior Peak Hour<br>Performance</h2>
      <p class="feature-text">Only Tern Netlink prioritises different types of traffic, allowing streaming, surfing or gaming to run seamlessly all the time.</p>
    </article>
  </section>

  <nav class="footer-nav">
    <a href="#">home</a><a href="#">products</a><a href="#">promos</a>
    <a href="#">pricing</a><a href="#">support</a><a href="#">contact</a>
  </nav>
  <p class="footer-contact">Questions? Call our 24/7 hotline <strong>6400 2917</strong> or visit one of our retail outlets.</p>
</body>
</html>
```